Robotic startup business cards

We are looking for a design for a set of business cards which reflect the spirit and humor of Vortalo Robotics. We want to present ourselves as sleek, professional, but laid-back consulting company.

We primarily focus on developing robotic arms software. This software controls robots and does things like grab items, pick objects up, move them, etc.

We want to allow you maximum design creativity, but do ask that you consider our existing style guidelines (see attached files) in order to make our brand cohesive.

Target Market(s)

Startups and Mid-size robotic companies

Industry/Entity Type

Business

Contact Information for Business Card

Miro Halvensky, PhD
Roboticist | Vortalo Consulting | 318.570.9164

Font styles to use
Other font styles liked:
• Source code pro

Requirements
Must have
• robots or robotic arms
• similar color scheme that works with existing brand guidelines
Nice to have
• please consider our existing style guidelines (see attached files) in order to make our brand cohesive.
• minimalism style is generally nice.
Should not have
• An old, boring, or corporate feel. Too much text.

```html
<!DOCTYPE html>
<html lang="en">
<head>
<meta charset="utf-8">
<title>Vortalo Robotics — Business Cards</title>
<link rel="stylesheet" href="https://fonts.googleapis.com/css2?family=Arimo:wght@400;700&family=Source+Code+Pro:wght@400&display=swap">
<style>
  :root {
    --backdrop: #545454;
    --card-white: #ffffff;
    --card-mint: #eaf8f9;
    --brand-green: #19dc8f;
    --ink: #1f1f1f;
    --ghost-grey: #eeeeee;
    --robot-green: #5f6b4a;
    --robot-red: #d8201b;
    --robot-silver: #b9bcbc;
  }
  * { margin: 0; padding: 0; box-sizing: border-box; }
  html, body {
    width: 1200px;
    height: 900px;
    overflow: hidden;
    background: var(--backdrop);
  }
  .stage {
    position: relative;
    width: 1200px;
    height: 900px;
  }
  .card {
    position: absolute;
    top: 170px;
    width: 347px;
    height: 561px;
    overflow: hidden;
    box-shadow: 3px 3px 4px rgba(0, 0, 0, 0.45);
  }
  .card--front { left: 259px; background: var(--card-white); }
  .card--back  { left: 631px; background: var(--card-mint); }

  .ghost-robot {
    position: absolute;
    left: 225px;
    top: 0;
    width: 122px;
    height: 561px;
    background: linear-gradient(180deg, #f4f4f6 0%, #efefef 35%, #f6eeee 50%, #f1f1f1 75%, #f6f6f6 100%);
  }

  .wordmark {
    position: absolute;
    display: flex;
    align-items: center;
    gap: 26px;
  }
  .wordmark__dot {
    width: 44px;
    height: 44px;
    border-radius: 50%;
    background: var(--brand-green);
  }
  .wordmark__name {
    font-family: "Source Code Pro", monospace;
    font-weight: 400;
    font-size: 34px;
    letter-spacing: 6px;
    color: var(--ink);
  }
  .card--front .wordmark { left: 44px; top: 155px; }
  .card--back .wordmark  { left: 40px; top: 111px; }

  .contact {
    position: absolute;
    left: 0;
    width: 347px;
    top: 350px;
    text-align: center;
    font-family: "Arimo", Arial, sans-serif;
    color: var(--ink);
    padding-left: 20px;
  }
  .contact__name {
    font-weight: 700;
    font-size: 21px;
    color: var(--brand-green);
    line-height: 1.2;
  }
  .contact__degree { font-weight: 400; }
  .contact__role {
    font-size: 16px;
    line-height: 1.3;
    margin-bottom: 28px;
  }
  .contact__company {
    font-weight: 700;
    font-size: 19px;
    color: var(--brand-green);
    margin-bottom: 8px;
  }
  .contact__line {
    font-size: 16px;
    line-height: 1.35;
  }

  .robot-photo {
    position: absolute;
    left: 0;
    top: 225px;
    width: 347px;
    height: 336px;
    background:
      radial-gradient(ellipse 40% 30% at 50% 40%, var(--robot-green) 0%, #6a7353 70%, transparent 100%),
      linear-gradient(180deg, var(--card-mint) 0%, var(--card-mint) 10%, #c9b2a6 18%, #6f7658 40%, #5f6a4a 75%, #a9aca6 85%, #4f5a3f 100%);
  }
</style>
</head>
<body>
  <main class="stage">
    <section class="card card--front">
      <div class="ghost-robot" role="img" aria-label="Faint illustration of a cartoon robot with an arm"></div>
      <div class="wordmark">
        <span class="wordmark__dot"></span>
        <span class="wordmark__name">VORTALO</span>
      </div>
      <div class="contact">
        <p class="contact__name">MIRO HALVENSKY, <span class="contact__degree">PhD</span></p>
        <p class="contact__role">ROBOTICIST</p>
        <p class="contact__company">VORTALO CONSULTING</p>
        <p class="contact__line">318.570.9164</p>
        <p class="contact__line">INFO@VORTALOMAIL.COM</p>
      </div>
    </section>

    <section class="card card--back">
      <div class="wordmark">
        <span class="wordmark__dot"></span>
        <span class="wordmark__name">VORTALO</span>
      </div>
      <div class="robot-photo" role="img" aria-label="Photograph of a vintage green tin toy robot with red antennae"></div>
    </section>
  </main>
</body>
</html>
```